Hearth Keepers Brochure - marketing an innovative home maintenance subscription program

We would like a brochure for this new service offering.
Hearth Keepers offers a subscription based home maintenance program that is quite unique. Everyone goes to the dentist for regular checkups and cleanings, or takes their car for oil changes, but too few pay that much attention to their largest asset - their home. So we fill that niche. We need a good brochure to promote the quarterly maintenance and our general contracting services.

Target Market(s)

Upper-Middle Class, SF Bay Area, Home Owner. Techies without know-how or time, single women, and elderly families or those with vacation homes.

Industry/Entity Type

Handyman and general contracting (residential construction and maintenance)

Font styles to use
Serif

Colors
0054AA
0677BA
7BADD7
CADEEF
E8F1F8

Requirements
Must have
• Basic contact info for www.HearthKeepers.example, some sort of hook, logo, etc.
Nice to have
• Something awesome!
Should not have
• Want classy, not cheap or flashy. Must have good balance for high-end homeowners in San Francisco Bay Area.

```html
<!DOCTYPE html>
<html lang="en">
<head>
<meta charset="utf-8">
<title>Hearth Keepers Brochure</title>
<link href="https://fonts.googleapis.com/css2?family=Oswald:wght@500;600&family=Montserrat:wght@400;500;600;700&display=swap" rel="stylesheet">
<style>
:root{
  --navy:#233f96;
  --orange:#ee5a24;
  --green:#6aa42f;
  --gold:#f4b400;
  --bullet-gold:#f7c531;
  --ink:#2a2a2a;
  --paper:#ffffff;
  --stage:#eef0f3;
  --badge:#dfe6f3;
}
*{box-sizing:border-box;margin:0;padding:0}
html,body{width:1050px;height:1200px;overflow:hidden}
body{background:var(--stage);position:relative;font-family:'Montserrat',sans-serif;color:var(--ink)}
.page{position:absolute;top:246px;width:500px;height:708px;background:var(--paper);overflow:hidden;box-shadow:0 2px 10px rgba(0,0,0,.12)}
.page--front{left:16px}
.page--back{left:534px}
.shapes{position:absolute;inset:0;width:500px;height:708px}
.brand{position:absolute;left:30px;top:24px}
.brand__row{display:flex;align-items:center;gap:8px}
.brand__square{width:34px;height:34px;background:var(--navy)}
.brand__name{font-family:'Oswald',sans-serif;font-weight:600;font-size:21px;line-height:.98;color:var(--navy)}
.brand__tagline{margin-top:5px;font-size:6px;font-weight:700;color:var(--ink)}

.headline{position:absolute;left:0;right:0;top:352px;text-align:center;font-family:'Oswald',sans-serif;font-weight:500;line-height:1.08}
.headline__name{font-size:40px;color:var(--navy)}
.headline__offer{font-size:25px;color:var(--orange)}
.headline__program{display:block;font-size:26px;color:var(--green)}

.gold-bullets{position:absolute;left:14px;top:471px;list-style:none;font-size:10.4px;line-height:13.4px;color:var(--bullet-gold);white-space:nowrap}
.gold-bullets li{position:relative;padding-left:13px;margin-bottom:12px}
.gold-bullets li::before{content:"•";position:absolute;left:0}

.front-copy{position:absolute;left:246px;top:461px;font-size:10px;line-height:13.4px;white-space:nowrap}
.front-copy p{margin-bottom:11px}

.partner{position:absolute;right:16px;bottom:16px;display:flex;align-items:center;gap:5px}
.partner__square{width:18px;height:18px;background:var(--navy)}
.partner__name{font-family:'Oswald',sans-serif;font-weight:500;font-size:12px;color:var(--navy)}

.back-copy{position:absolute;left:19px;top:111px;font-size:10px;line-height:12.2px;white-space:nowrap}
.back-copy p{margin-bottom:12px}

.panel-copy{position:absolute;left:19px;top:412px;color:#fff;font-size:10px;line-height:12.2px;white-space:nowrap}
.panel-copy p{margin-bottom:12px}
.panel-copy ul{list-style:none;color:var(--bullet-gold);margin-top:16px}
.panel-copy li{position:relative;padding-left:11px;margin-bottom:8px}
.panel-copy li::before{content:"•";position:absolute;left:0}

.info{position:absolute;left:258px;top:520px;width:230px;text-align:center;font-size:9.8px;line-height:12.2px;white-space:nowrap}
.info__title{font-size:11.5px;font-weight:700;color:var(--navy);text-decoration:underline;margin-bottom:12px}
.info__label{margin-top:12px}
.info__url{margin-top:4px;font-size:14px;font-weight:700;color:var(--orange)}
.info__phone{margin-top:9px;font-size:14px;font-weight:700;color:var(--orange)}
</style>
</head>
<body>

<section class="page page--front" aria-label="Brochure front">
  <svg class="shapes" viewBox="0 0 500 708">
    <defs>
      <linearGradient id="familyTone" x1="0" y1="0" x2="1" y2="1">
        <stop offset="0" stop-color="#6e7e93"/><stop offset="1" stop-color="#3f4a5c"/>
      </linearGradient>
      <linearGradient id="gutterTone" x1="0" y1="0" x2="1" y2="1">
        <stop offset="0" stop-color="#2f3a55"/><stop offset=".5" stop-color="#c9c3a8"/><stop offset="1" stop-color="#3b6fc0"/>
      </linearGradient>
    </defs>
    <rect x="0" y="91" width="230" height="236" fill="url(#familyTone)" role="img" aria-label="Photo of a family reading together at home"/>
    <polygon points="254,0 500,0 500,343 272,343 168,182" fill="url(#gutterTone)" role="img" aria-label="Photo of a technician on a ladder cleaning a roof gutter"/>
    <polyline points="246,300 272,348 440,350" fill="none" stroke="var(--gold)" stroke-width="2"/>
    <path d="M0,444 H196 Q204,444 208,451 L236,505 L165,708 H0 Z" fill="var(--navy)"/>
  </svg>

  <header class="brand">
    <div class="brand__row"><span class="brand__square"></span><span class="brand__name">HEARTH<br>KEEPERS</span></div>
    <p class="brand__tagline">We maintain your home, so you don’t have to.</p>
  </header>

  <h1 class="headline">
    <span class="headline__name">HEARTH KEEPERS</span>
    <span class="headline__offer">OFFERS AN AMAZING</span>
    <span class="headline__program">PROACTIVE MAINTENANCE PROGRAM.</span>
  </h1>

  <ul class="gold-bullets">
    <li>Our GC Division manages any<br>larger repairs or “special<br>projects.”</li>
    <li>Financial advisors recommend<br>budgeting 1-4% of the value of<br>a home for annual maintenance.</li>
    <li>Hearth Keeping is the most<br>cost-efficient way to maintain<br>your home.</li>
    <li>Let us maintain your home,<br>so you don’t have to.</li>
  </ul>

  <div class="front-copy">
    <p>We keep one of your largest assets in great<br>condition, and let you enjoy your weekends.<br>This system has been perfected for over 20<br>years.</p>
    <p>Here’s how it works. During an initial intake<br>inspection we inventory all major systems and<br>appliances, and generate a punch list of any<br>deferred maintenance. Using this information<br>we can respond more quickly when things<br>break, and we create a roadmap to address<br>any problems.</p>
    <p>Then, using seasonal checklists, a two-person<br>team inspects and repairs over 250 items<br>annually.</p>
  </div>

  <div class="partner"><span class="partner__square"></span><span class="partner__name">SOUND DWELLING LABS</span></div>
</section>

<section class="page page--back" aria-label="Brochure back">
  <svg class="shapes" viewBox="0 0 500 708">
    <defs>
      <linearGradient id="gridTone" x1="0" y1="0" x2="1" y2="1">
        <stop offset="0" stop-color="#a89a86"/><stop offset=".5" stop-color="#8a7f70"/><stop offset="1" stop-color="#5f6670"/>
      </linearGradient>
      <clipPath id="gridClip"><polygon points="325,0 500,0 500,342 346,342 236,153"/></clipPath>
    </defs>
    <polygon points="325,0 500,0 500,342 346,342 236,153" fill="url(#gridTone)" role="img" aria-label="Grid of photos showing home repairs, plumbing, decking, HVAC filters and ductwork"/>
    <g stroke="#fff" stroke-width="2" clip-path="url(#gridClip)">
      <line x1="386" y1="0" x2="386" y2="342"/>
      <line x1="230" y1="58" x2="500" y2="58"/>
      <line x1="230" y1="134" x2="500" y2="134"/>
      <line x1="230" y1="210" x2="500" y2="210"/>
      <line x1="230" y1="286" x2="500" y2="286"/>
    </g>
    <polygon points="311,0 325,0 236,153 346,342 332,342 222,153" fill="var(--navy)"/>
    <path d="M0,401 H222 Q232,401 237,409 L281,492 L193,708 H0 Z" fill="var(--navy)"/>
    <circle cx="307" cy="443" r="25" fill="var(--badge)" role="img" aria-label="Illustration of a handyman with tools"/>
    <circle cx="378" cy="443" r="25" fill="var(--badge)" role="img" aria-label="Illustration of a worker at a ladder"/>
    <rect x="362" y="403" width="32" height="8" rx="2" fill="#8a8f99"/>
    <circle cx="449" cy="443" r="25" fill="var(--badge)" role="img" aria-label="Illustration of a technician cleaning"/>
    <circle cx="436" cy="461" r="11" fill="var(--navy)"/>
  </svg>

  <header class="brand">
    <div class="brand__row"><span class="brand__square"></span><span class="brand__name">HEARTH<br>KEEPERS</span></div>
    <p class="brand__tagline">We maintain your home, so you don’t have to.</p>
  </header>

  <div class="back-copy">
    <p>We maintain your home, so you<br>don’t have to.</p>
    <p>You take your car in for oil changes.</p>
    <p>You go to the dentist for check-ups.</p>
    <p>But when was the last time you had your<br>home inspected, or managed, to check over<br>250 items off your to-do list?</p>
    <p>Hearth Keeping is a philosophy and lifestyle<br>change.</p>
    <p>We keep your largest asset in great condition, and let<br>you take back your weekends.</p>
    <p>Our unique subscription service combines quarterly<br>inspections and handyman repairs.</p>
    <p>Don’t climb that rickety ladder to clean your gutters or start projects you can’t finish.</p>
    <p>Our team is ready to care for your home.</p>
  </div>

  <div class="panel-copy">
    <p>Perhaps it’s worth having at least one of<br>the panels dedicated to specific “Special<br>Projects” or “General Contracting” services<br>that we like to specialize in.</p>
    <p>Hearth Keepers can also help with larger<br>home improvements such as:</p>
    <ul>
      <li>Kitchen and bath remodels</li>
      <li>New landscape installations and decks</li>
      <li>New roofs, siding, doors and windows</li>
      <li>Site drainage</li>
      <li>Home comfort and HVAC upgrades</li>
      <li>Indoor air quality improvements</li>
    </ul>
  </div>

  <div class="info">
    <p class="info__title">General INFO:</p>
    <p>Hearth Keepers is a (residential handyman<br>and general contracting) division of<br>Sound Dwelling Labs<br>(www.sounddwellinglabs.example). We<br>are a Civic Trust Co.</p>
    <p class="info__label">Contact info:</p>
    <p class="info__url">www.HearthKeepers.example</p>
    <p class="info__phone">415-555-0142</p>
  </div>
</section>

</body>
</html>
```